Armored courier complete website design
HALVORSEN
Armored courier complete website design - Security
Creative Brief
Security
www.halvorsenllc.example
Local armored transportation company for packages, documents, deposits, ATM's and banks. quillmark77 created original logo and personal font from pellavine. SERVICES OFFERED BY THE HALVORSEN COMPANY (1.) Courier (a.) Cash Logistics (i.) Critical Delivery (ii.) Armored Courier Services (b.) Pharmaceutical (c.) Medical Logistics (d.) Retail & Commercial Deposit Delivery & Change Order Return Service (e.) Legal (i.) Document Delivery (ii.) Critical Courier (2.) ATM Services (a.) Installation & Removal (b.) Cash Replenishment & Deposit Removal (c.) Maintenance & Repair (i.) First Line (d.) Physical Surroundings Repair (i.) Carousel (ii.) Signage (iii.) Pilons (e.) Custom ATM Branding Solutions (f.) ATM Cleaning & Detailing (3.) Security Guard Services (a.) Corporate Security (b.) Industrial (c.) Retail (d.) Tourism & Special Events (4.) Investigative Services (a.) Corporate Investigations (b.) Workers’ Compensation Fraud Investigations (c.) Retail & Industrial (5.) Secure-Area Cleaning Services (a.) Banks & Credit Unions (b.) Industrial & Commercial (6.) Logistics (a.) Contract Logistics (b.) Critical Parts & Product Logistics (7.) Document Destruction (a.) Scheduled Programs (b.) Short term, Single Project
Would like a design similar to Vellmora.com but feel free to expand from that idea. Centralized text box for images and information. Promote strength through imagery. Do not want a cookie cutter site like everyone else, i.e. Kestrin and Ostley
left side
www.vellmora.com
http://www.kestrinworld.example/cash-services/en
http://ostleyvaulted.example/
Copy for each subject can be provided. Kestrinworld has a good layout of services provided, company, careers, contact us Contact us is very important -Company -Services - - - -Careers -Contact us
Halvorsen Halvorsen
The instructions provided with our latest brief updates should assist everyone in tweaking and completing the HALVORSEN design. The simplicity and elegance similar to vellmora.com is all we're after. Clean lines, dark shading, stainless steel used as indicated, watermarks, chiseled edging, sharp relative images and clear/smoked borders placed as directed is what we are currently seeking. Thank you much for your efforts to date and we look forward to seeing everyone's updates per the brief updates provided below.
#96 is closest to what we are looking for. The center, scrolling buttons would be a little smaller, no border but suspended with a white, small description text at the top of each. The large, background image would have a small text description at the upper right only. This description/button could be clicked on in reference to the photo for navigation purposes. Thank you for your hard work. Much appreciated.
The bottom of the page should be entirely black with a slight fade at the top. This should cover the entire bottom of the page and be about a quarter to 1/3rd in height. The side bar should slightly bleed into this dark space. Only very small text disclosures, etc. will be placed in this black area. Thank you.
Please, no shield references at top of the navigation bar. Rectangular only. Thank you in advance.
Also, on the side, navigation bar please only put the name HALVORSEN at the top and utilize our logo at the bottom in a darker, chiseled watermark. The company name should be separated from the navigation bars via a thin line. Border the side bar identical to draft #96, i.e. transparent, and use the same darker, shaded stainless steel background behind all text as draft #96. In addition, the emphasis will be on scrolling images in the background so the width and text of navigation side bar can smaller and tighter but longer in length. Thank you for your efforts!
#96 is closest so far to what we are looking for. Left navigation bar is key. Refer all designs to Vellmora.com this is the look we are going for. Spend the time on the little things, a simple design that we are looking for only works with with high quality nav bars and animation. Thank you all for your hard work!

```html
<!DOCTYPE html>
<html lang="en">
<head>
<meta charset="utf-8">
<title>HALVORSEN – Armored Courier &amp; Security</title>
<link rel="stylesheet" href="https://fonts.googleapis.com/css2?family=Lato:wght@300;400;700&family=Montserrat:wght@400;600;700&display=swap">
<style>
  :root {
    --sky-top: #3f5a7c;
    --sky-mid: #7c97b8;
    --sky-light: #a9c6e4;
    --city-warm: #9a6a3c;
    --city-dark: #2a2a2e;
    --black: #0a0a0a;
    --white: #ffffff;
    --grey-text: #8a8a8a;
    --steel-light: #6e6e6e;
    --steel-mid: #4a4a4a;
    --steel-dark: #2c2c2c;
    --frame: rgba(150,150,150,0.45);
  }
  * { margin: 0; padding: 0; box-sizing: border-box; }
  html, body { width: 1200px; height: 773px; overflow: hidden; background: var(--black); }
  .page {
    position: relative; width: 1200px; height: 773px; overflow: hidden;
    font-family: 'Lato', sans-serif; color: var(--white);
  }
  .hero-image {
    position: absolute; left: 0; top: 0; width: 1200px; height: 560px;
    background:
      radial-gradient(ellipse 300px 200px at 520px 380px, rgba(210,140,70,0.55), transparent 70%),
      radial-gradient(ellipse 260px 160px at 1130px 360px, rgba(220,120,50,0.5), transparent 70%),
      linear-gradient(180deg, var(--sky-top) 0%, var(--sky-mid) 30%, var(--sky-light) 45%, var(--city-warm) 65%, var(--city-dark) 85%, var(--black) 100%);
  }
  .bottom-shade {
    position: absolute; left: 0; top: 470px; width: 1200px; height: 303px;
    background: linear-gradient(180deg, rgba(10,10,10,0) 0%, rgba(10,10,10,0.85) 18%, var(--black) 22%, var(--black) 100%);
  }
  .hero-caption {
    position: absolute; right: 17px; top: 14px; text-align: right;
  }
  .hero-caption .kicker { font-weight: 700; font-size: 14px; color: #111; margin-right: 34px; }
  .hero-caption .title { font-weight: 700; font-size: 18px; color: #111; margin-top: 10px; }

  .side-nav {
    position: absolute; left: 60px; top: 75px; width: 193px; height: 487px;
    background: var(--frame); padding: 9px 8px;
  }
  .side-nav-inner {
    position: relative; width: 100%; height: 100%;
    background:
      repeating-linear-gradient(0deg, rgba(255,255,255,0.03) 0 1px, rgba(0,0,0,0.04) 1px 3px),
      linear-gradient(180deg, var(--steel-dark) 0%, var(--steel-mid) 45%, var(--steel-light) 100%);
  }
  .brand-name {
    position: absolute; left: 0; top: 20px; width: 100%; text-align: center;
    font-family: 'Montserrat', sans-serif; font-weight: 700; font-size: 21px;
    letter-spacing: 1px; color: #d8d8d8;
  }
  .brand-rule { position: absolute; left: 0; top: 56px; width: 100%; height: 1px; background: rgba(255,255,255,0.25); }
  .nav-list { position: absolute; left: 9px; top: 82px; width: 157px; list-style: none; }
  .nav-item {
    height: 30px; margin-bottom: 4.5px; padding-right: 6px; line-height: 30px; text-align: right;
    font-family: 'Montserrat', sans-serif; font-weight: 600; font-size: 12.5px; color: var(--white);
  }
  .nav-item.is-active { background: linear-gradient(90deg, #000 0%, #1a1a1a 60%, #555 100%); }
  .nav-watermark {
    position: absolute; left: 20px; top: 350px; width: 136px; height: 136px;
    background: rgba(0,0,0,0.12); display: flex; align-items: center; justify-content: center;
    font-family: 'Montserrat', sans-serif; font-weight: 700; font-size: 18px; color: rgba(0,0,0,0.22);
  }

  .service-strip { position: absolute; left: 462px; top: 474px; display: flex; gap: 5.4px; }
  .service { width: 71px; text-align: center; }
  .service-label {
    height: 27px; display: flex; align-items: flex-end; justify-content: center;
    font-family: 'Montserrat', sans-serif; font-size: 10px; line-height: 11.5px; color: var(--white);
  }
  .service-photo { width: 71px; height: 57px; margin-top: 2px; }
  .service-reflection { width: 71px; height: 36px; margin-top: 7px; opacity: 0.35;
    -webkit-mask-image: linear-gradient(180deg, #000, transparent); mask-image: linear-gradient(180deg, #000, transparent); }
  .tone-courier { background: linear-gradient(160deg, #8a6a4a, #c9a27a); }
  .tone-atm { background: linear-gradient(160deg, #9aa3ab, #d7d9db); }
  .tone-guard { background: linear-gradient(160deg, #6f9fd0, #3b5a2a); }
  .tone-investigate { background: linear-gradient(160deg, #d8e2ea, #8fa9c4); }
  .tone-cleaning { background: linear-gradient(160deg, #c98a3e, #9fa6aa); }
  .tone-logistics { background: linear-gradient(160deg, #7fb2d8, #1f5d86); }
  .tone-destruction { background: linear-gradient(160deg, #a9b6c2, #5d7088); }

  .footer-address { position: absolute; left: 84px; top: 682px; display: flex; gap: 7px;
    font-weight: 300; font-size: 11.5px; line-height: 16.5px; }
  .footer-brand { position: absolute; left: 0; width: 1200px; top: 700px; text-align: center;
    font-family: 'Montserrat', sans-serif; font-weight: 700; font-size: 22px; letter-spacing: 2px; color: #6a6a6a; }
  .footer-copy { position: absolute; left: 0; width: 1200px; top: 742px; text-align: center;
    font-size: 11.5px; color: var(--grey-text); }
  .footer-contact { position: absolute; left: 976px; top: 680px; }
  .contact-line { display: flex; align-items: center; gap: 10px; }
  .contact-line.phone { font-weight: 700; font-size: 15px; }
  .contact-line.email { font-size: 12.5px; margin-top: 14px; }
</style>
</head>
<body>
<main class="page">
  <div class="hero-image" role="img" aria-label="City skyline at dusk with lit towers and an arched bridge"></div>
  <div class="bottom-shade"></div>

  <div class="hero-caption">
    <p class="kicker">Lorem ipsum dolor</p>
    <p class="title">Consectetur Adipiscing</p>
  </div>

  <nav class="side-nav">
    <div class="side-nav-inner">
      <div class="brand-name">HALVORSEN</div>
      <div class="brand-rule"></div>
      <ul class="nav-list">
        <li class="nav-item is-active">HOME</li>
        <li class="nav-item">ABOUT US</li>
        <li class="nav-item">SERVICES</li>
        <li class="nav-item">CAREERS</li>
        <li class="nav-item">CONTACT US</li>
      </ul>
      <div class="nav-watermark">HALVORSEN</div>
    </div>
  </nav>

  <section class="service-strip">
    <div class="service"><div class="service-label">Courier</div><div class="service-photo tone-courier" role="img" aria-label="Couriers handling packages"></div><div class="service-reflection tone-courier"></div></div>
    <div class="service"><div class="service-label">ATM<br>Services</div><div class="service-photo tone-atm" role="img" aria-label="Customer at an ATM"></div><div class="service-reflection tone-atm"></div></div>
    <div class="service"><div class="service-label">Security Guard<br>Services</div><div class="service-photo tone-guard" role="img" aria-label="Security guard on patrol"></div><div class="service-reflection tone-guard"></div></div>
    <div class="service"><div class="service-label">Investigative<br>Services</div><div class="service-photo tone-investigate" role="img" aria-label="Investigators in a laboratory"></div><div class="service-reflection tone-investigate"></div></div>
    <div class="service"><div class="service-label">Secure-Area<br>Cleaning</div><div class="service-photo tone-cleaning" role="img" aria-label="Secure keypad on a door"></div><div class="service-reflection tone-cleaning"></div></div>
    <div class="service"><div class="service-label">Logistics</div><div class="service-photo tone-logistics" role="img" aria-label="Cargo ship at sea"></div><div class="service-reflection tone-logistics"></div></div>
    <div class="service"><div class="service-label">Document<br>Destruction</div><div class="service-photo tone-destruction" role="img" aria-label="People reviewing documents"></div><div class="service-reflection tone-destruction"></div></div>
  </section>

  <footer>
    <div class="footer-address">
      <svg width="11" height="15" viewBox="0 0 11 15" aria-hidden="true"><path d="M5.5 0C2.5 0 0 2.4 0 5.4 0 9.5 5.5 15 5.5 15S11 9.5 11 5.4C11 2.4 8.5 0 5.5 0z" fill="#fff"/><circle cx="5.5" cy="5.3" r="2" fill="#0a0a0a"/></svg>
      <p>123&nbsp; Lorem Sum Dolor<br>Sit Amet Consectuer<br>Adipiscing Elit</p>
    </div>
    <div class="footer-brand">HALVORSEN</div>
    <p class="footer-copy">© 2015 Halvorsenllc. All Rights Reserved</p>
    <div class="footer-contact">
      <div class="contact-line phone">
        <svg width="9" height="14" viewBox="0 0 9 14" aria-hidden="true"><rect x="0.5" y="0.5" width="8" height="13" rx="1.5" fill="none" stroke="#fff"/><rect x="2" y="2.5" width="5" height="7" fill="#fff"/></svg>
        (123) 456-7890
      </div>
      <div class="contact-line email">
        <svg width="13" height="9" viewBox="0 0 13 9" aria-hidden="true"><rect width="13" height="9" fill="#fff"/><path d="M0 0l6.5 5L13 0" fill="none" stroke="#0a0a0a"/></svg>
        info@yourEmail.com
      </div>
    </div>
  </footer>
</main>
</body>
</html>
```